kvt business card

need clean and modern business card design, possibly two. Logo on front and writing on back-Full source files for logo attached-THE CHOSEN LOGO IS SQUARE KVT with KVT HOLDINGS in ALL BLUE. Please do not use any other logos from files, this is source file that includes correct logo

```html
<!DOCTYPE html>
<html lang="en">
<head>
<meta charset="UTF-8">
<title>KVT Holdings Business Card</title>
<link href="https://fonts.googleapis.com/css2?family=Michroma&family=Open+Sans:wght@400;600&display=swap" rel="stylesheet">
<style>
  :root {
    --backdrop: #97bcc1;
    --paper: #f2f2f0;
    --brand-blue: #2e6db4;
    --white: #ffffff;
  }
  html, body {
    margin: 0;
    width: 1200px;
    height: 960px;
    overflow: hidden;
    background: var(--backdrop);
  }
  .canvas {
    position: relative;
    width: 1200px;
    height: 960px;
  }
  .card {
    position: absolute;
    left: 250px;
    width: 700px;
    height: 400px;
    background: var(--paper);
    overflow: hidden;
    box-shadow: 0 6px 18px rgba(0, 0, 0, 0.12);
  }
  .card-front { top: 50px; }
  .card-back { top: 500px; }
  .card svg.shape {
    position: absolute;
    inset: 0;
  }
  .front-mark {
    position: absolute;
    left: 0;
    right: 0;
    top: 150px;
    display: flex;
    justify-content: center;
    align-items: center;
    gap: 22px;
  }
  .mark-square {
    width: 70px;
    height: 70px;
    border: 6px solid var(--brand-blue);
    box-sizing: border-box;
  }
  .wordmark {
    font-family: "Michroma", sans-serif;
    color: var(--brand-blue);
    font-size: 40px;
    letter-spacing: 2px;
    line-height: 1;
  }
  .back-mark {
    position: absolute;
    left: 40px;
    top: 150px;
    display: flex;
    align-items: center;
    gap: 14px;
  }
  .back-mark .mark-square {
    width: 40px;
    height: 40px;
    border: 4px solid var(--white);
  }
  .back-mark .wordmark {
    color: var(--white);
    font-size: 24px;
    letter-spacing: 1px;
  }
  .identity {
    position: absolute;
    left: 395px;
    top: 70px;
    width: 240px;
    font-family: "Open Sans", sans-serif;
    color: var(--white);
  }
  .person-name {
    font-size: 32px;
    line-height: 1.1;
    padding-bottom: 4px;
    border-bottom: 1.5px solid var(--white);
  }
  .person-role {
    font-size: 17px;
    margin-top: 6px;
  }
  .contact-list {
    position: absolute;
    left: 395px;
    top: 218px;
    margin: 0;
    padding: 0;
    list-style: none;
    font-family: "Open Sans", sans-serif;
    color: var(--brand-blue);
    font-size: 14px;
  }
  .contact-item {
    display: flex;
    align-items: center;
    gap: 12px;
    height: 38px;
  }
  .contact-item svg { flex: none; }
  .contact-text {
    width: 185px;
    padding-bottom: 3px;
    border-bottom: 2px dotted var(--brand-blue);
  }
</style>
</head>
<body>
<main class="canvas">

  <section class="card card-front" aria-label="Card front">
    <svg class="shape" width="700" height="400" viewBox="0 0 700 400">
      <path d="M0 90 H10 A30 30 0 0 1 40 120 V280 A30 30 0 0 1 10 310 H0 Z" fill="var(--brand-blue)"/>
      <path d="M700 90 H690 A30 30 0 0 0 660 120 V280 A30 30 0 0 0 690 310 H700 Z" fill="var(--brand-blue)"/>
    </svg>
    <div class="front-mark">
      <span class="mark-square"></span>
      <span class="wordmark">KVT HOLDINGS</span>
    </div>
  </section>

  <section class="card card-back" aria-label="Card back">
    <svg class="shape" width="700" height="400" viewBox="0 0 700 400">
      <path d="M0 40 H700 V190 H420 C370 190 370 310 310 310 H0 Z" fill="var(--brand-blue)"/>
      <path d="M0 120 H8 A28 28 0 0 1 36 148 V222 A28 28 0 0 1 8 250 H0 Z" fill="var(--paper)"/>
      <path d="M700 225 H692 A28 28 0 0 0 664 253 V320 A28 28 0 0 0 692 348 H700 Z" fill="var(--brand-blue)"/>
    </svg>

    <div class="back-mark">
      <span class="mark-square"></span>
      <span class="wordmark">KVT HOLDINGS</span>
    </div>

    <div class="identity">
      <div class="person-name">Your Name</div>
      <div class="person-role">Designation</div>
    </div>

    <ul class="contact-list">
      <li class="contact-item">
        <svg width="20" height="24" viewBox="0 0 20 24"><path d="M10 1 C5 1 2 5 2 9 C2 15 10 23 10 23 C10 23 18 15 18 9 C18 5 15 1 10 1 Z" fill="var(--brand-blue)"/><circle cx="10" cy="9" r="3.5" fill="var(--paper)"/></svg>
        <span class="contact-text">Your Address</span>
      </li>
      <li class="contact-item">
        <svg width="20" height="24" viewBox="0 0 20 24"><rect x="4" y="1" width="12" height="22" rx="2" fill="none" stroke="var(--brand-blue)" stroke-width="2"/><line x1="4" y1="18" x2="16" y2="18" stroke="var(--brand-blue)" stroke-width="1.5"/></svg>
        <span class="contact-text">+01 xxxx xxxx xxx</span>
      </li>
      <li class="contact-item">
        <svg width="20" height="24" viewBox="0 0 20 24"><rect x="1" y="6" width="18" height="13" fill="var(--brand-blue)"/><path d="M1 6 L10 14 L19 6" fill="none" stroke="var(--paper)" stroke-width="1.5"/></svg>
        <span class="contact-text">youremail@mailbox.com</span>
      </li>
      <li class="contact-item">
        <svg width="20" height="24" viewBox="0 0 20 24"><circle cx="10" cy="12" r="9" fill="var(--brand-blue)"/><g stroke="var(--paper)" stroke-width="1" fill="none"><ellipse cx="10" cy="12" rx="4" ry="9"/><line x1="1" y1="12" x2="19" y2="12"/><line x1="10" y1="3" x2="10" y2="21"/><line x1="3" y1="7.5" x2="17" y2="7.5"/><line x1="3" y1="16.5" x2="17" y2="16.5"/></g></svg>
        <span class="contact-text">www.WEBSITE.com</span>
      </li>
    </ul>
  </section>

</main>
</body>
</html>
```